Velvet Crumb by Marisol

Attached see my logo, i need to create a FB logo and banner to mirror my logo. My company does handcrafted and homemade gourmet pieces of heaven! Feel free to call me at 3127750146 or email me at marisol@velvetcrumb.com. Thank you. Marisol

```html
<!DOCTYPE html>
<html lang="en">
<head>
<meta charset="utf-8">
<title>Velvet Crumb by Marisol — Banner</title>
<link rel="stylesheet" href="https://fonts.googleapis.com/css2?family=Lobster&family=Roboto+Condensed:wght@400;500&display=swap">
<style>
  :root {
    --cream: #fbf8ec;
    --cocoa: #6b3f26;
    --blush: #efd6ea;
    --rose: #ee8fbb;
    --rose-soft: #f6b8d2;
    --mint: #8fd6cf;
    --lilac: #cdb3de;
    --ink: #2e2a2a;
  }
  html, body {
    margin: 0;
    padding: 0;
    overflow: hidden;
    background: var(--cream);
  }
  .banner {
    position: relative;
    width: 1200px;
    height: 447px;
    overflow: hidden;
    background: var(--cream);
  }
  .stripes {
    position: absolute;
    inset: 0;
  }
  .tagline-top {
    position: absolute;
    left: 20px;
    top: 14px;
    margin: 0;
    font-family: "Lobster", cursive;
    font-size: 44px;
    font-weight: 400;
    color: var(--cocoa);
    line-height: 1;
    transform: rotate(-2deg);
    transform-origin: left center;
  }
  .tagline-main {
    position: absolute;
    left: 14px;
    top: 74px;
    margin: 0;
    font-family: "Lobster", cursive;
    font-size: 196px;
    font-weight: 400;
    line-height: 1;
    color: var(--blush);
    -webkit-text-stroke: 5px var(--cocoa);
    paint-order: stroke fill;
    transform: rotate(-6deg);
    transform-origin: left center;
  }
  .cupcake-row {
    position: absolute;
    left: 200px;
    top: 225px;
    width: 575px;
    height: 205px;
    border-radius: 40px;
    background: linear-gradient(90deg, var(--mint) 0%, var(--lilac) 30%, var(--mint) 58%, var(--rose-soft) 80%, var(--mint) 100%);
    opacity: 0.7;
  }
  .brand-dot {
    position: absolute;
    left: 851px;
    top: 62px;
    width: 34px;
    height: 34px;
    border-radius: 50%;
    background: var(--rose);
  }
  .brand-name {
    position: absolute;
    left: 730px;
    top: 112px;
    width: 460px;
    margin: 0;
    text-align: center;
    font-family: "Roboto Condensed", sans-serif;
    font-weight: 400;
    font-size: 76px;
    line-height: 1;
    color: var(--rose);
  }
  .services,
  .order {
    position: absolute;
    left: 918px;
    margin: 0;
    font-family: "Roboto Condensed", sans-serif;
    font-weight: 400;
    color: var(--ink);
    line-height: 1.15;
  }
  .services {
    top: 290px;
    font-size: 18px;
    text-transform: uppercase;
  }
  .order {
    top: 372px;
    font-size: 16px;
  }
  .order .order-lead { text-transform: uppercase; font-size: 18px; }
</style>
</head>
<body>
<div class="banner">
  <svg class="stripes" width="1200" height="447" viewBox="0 0 1200 447" aria-hidden="true">
    <g class="stripes-upper">
      <rect x="846" y="0" width="7" height="40" fill="var(--rose-soft)"/>
      <rect x="860" y="0" width="4" height="40" fill="var(--rose)"/>
      <rect x="872" y="0" width="4" height="40" fill="var(--rose)"/>
      <rect x="883" y="0" width="7" height="40" fill="var(--rose-soft)"/>
    </g>
    <g class="stripes-lower">
      <rect x="846" y="240" width="7" height="207" fill="var(--rose-soft)"/>
      <rect x="860" y="240" width="4" height="207" fill="var(--rose)"/>
      <rect x="872" y="240" width="4" height="207" fill="var(--rose)"/>
      <rect x="883" y="240" width="7" height="207" fill="var(--rose-soft)"/>
    </g>
  </svg>

  <p class="tagline-top">Homemade Pieces of</p>
  <h1 class="tagline-main">Heaven</h1>

  <div class="cupcake-row" role="img" aria-label="Illustration of four pastel cupcakes with swirled frosting and sprinkles"></div>

  <span class="brand-dot" aria-hidden="true"></span>
  <p class="brand-name">Velvet Crumb</p>

  <p class="services">Cupcakes, cookies, &amp; treats.<br>Custom creations for<br>all your occasions.</p>

  <p class="order"><span class="order-lead">Order today @</span><br>312•775•0146 or e-mail<br>www.marisol@velvetcrumb.com</p>
</div>
</body>
</html>
```